Large Financial Advisory Firm Needs a Brochure!

We are looking for a modern and professional 4 page brochure for our Financial Advisory firm, Heronfield Capital Partners. I've attached multiple files to help with the completion of the design.
SIZE OF BROCHURE: 17 x 11 FLAT, 8.5 x 11 inch FOLDED
1. A PDF titled Design Brief will provide you with an overview of the project, the text to be included in the brochure and other misc. instructions.
2. Logo Files, you will need to incorporate our logo into the brochure design, I've attached all the files please select the images that suit your design.
3. Competitor Illustration - I've attached an image that needs to be included on the 2nd page (inside left cover of the brochure). You will need to incorporate the pros/cons of using our competitors and the advantages of using our firm. This is outlined in the Design Brief PDF.
NOTE: If possible please get rid of the blue sky in the illustration. Just use the buildings, the blue throws off the concept. I contacted the illustrator and am waiting for a design without the sky but it may not be ready in time so please delete it if possible.
- I like the Avenir fonts, 85 Heavy, 65 Medium and 45.

```html
<!DOCTYPE html>
<html lang="en">
<head>
<meta charset="utf-8">
<title>Heronfield Capital Partners – Brochure Cover</title>
<link rel="stylesheet" href="https://fonts.googleapis.com/css2?family=Nunito+Sans:wght@300;400;800&display=swap">
<style>
  :root {
    --paper: #ffffff;
    --sky-top: #5a9fdf;
    --sky-mid: #a6cdef;
    --sky-low: #dbe9f4;
    --meadow: #5aa52c;
    --swoosh-deep: #1a6fc4;
    --swoosh-light: #4fb0ee;
    --headline: #1f6aa8;
    --gold: #f4a21b;
    --gold-line: #e9b640;
    --ink: #1d1d1b;
  }
  * { margin: 0; padding: 0; box-sizing: border-box; }
  html, body {
    width: 809px;
    height: 1200px;
    overflow: hidden;
    background: var(--paper);
  }
  .cover {
    position: relative;
    width: 809px;
    height: 1200px;
    background: var(--paper);
    font-family: "Nunito Sans", Arial, sans-serif;
  }
  .hero-photo {
    position: absolute;
    left: 0; top: 0;
    width: 809px;
    height: 880px;
    background: linear-gradient(180deg,
      var(--sky-top) 0%,
      var(--sky-mid) 40%,
      var(--sky-low) 68%,
      var(--meadow) 100%);
  }
  .hero-rule {
    position: absolute;
    left: 0; top: 880px;
    width: 809px;
    height: 4px;
    background: var(--gold-line);
  }
  .swoosh {
    position: absolute;
    left: 0; top: 0;
    width: 809px;
    height: 330px;
  }
  .headline {
    position: absolute;
    right: 40px;
    top: 205px;
    text-align: right;
    color: var(--headline);
    font-weight: 300;
    line-height: 1.05;
  }
  .headline .kicker {
    display: block;
    font-size: 34px;
  }
  .headline .title {
    display: block;
    font-size: 58px;
  }
  .brand {
    position: absolute;
    left: 590px;
    top: 850px;
    width: 180px;
    text-align: center;
  }
  .brand-mark {
    width: 150px;
    height: 150px;
    margin: 0 auto;
    background: var(--gold);
    border: 6px solid var(--paper);
  }
  .brand-name {
    margin-top: 12px;
    color: var(--ink);
    font-weight: 800;
    font-size: 19px;
    line-height: 1.15;
    letter-spacing: 1px;
    text-transform: uppercase;
  }
  .footer-band {
    position: absolute;
    left: 0; bottom: 0;
    width: 809px;
    height: 24px;
    background: var(--gold);
  }
</style>
</head>
<body>
  <main class="cover">
    <div class="hero-photo" role="img" aria-label="Photo of cupped hands holding a pile of coins with a green seedling sprouting from them, in front of a blue sky and grassy hill"></div>
    <div class="hero-rule"></div>

    <svg class="swoosh" viewBox="0 0 809 330" aria-hidden="true">
      <defs>
        <linearGradient id="swooshFill" x1="0" y1="0" x2="1" y2="0.4">
          <stop offset="0" stop-color="#4fb0ee"/>
          <stop offset="0.5" stop-color="#1a6fc4"/>
          <stop offset="1" stop-color="#4fb0ee"/>
        </linearGradient>
      </defs>
      <path d="M0 0 H809 V95 C620 80 430 150 260 240 C170 285 80 300 0 290 Z" fill="url(#swooshFill)"/>
      <path d="M0 290 C80 300 170 285 260 240 C430 150 620 80 809 95" fill="none" stroke="#ffffff" stroke-width="10"/>
      <path d="M0 250 C120 250 250 180 380 110 C520 40 680 20 809 40" fill="none" stroke="#ffffff" stroke-opacity="0.35" stroke-width="3"/>
      <path d="M0 200 C140 190 260 120 400 60 C520 10 690 0 809 10" fill="none" stroke="#ffffff" stroke-opacity="0.25" stroke-width="2"/>
    </svg>

    <h1 class="headline">
      <span class="kicker">Redefining</span>
      <span class="title">Investment Advice</span>
    </h1>

    <div class="brand">
      <div class="brand-mark"></div>
      <p class="brand-name">Heronfield<br>Capital Partners</p>
    </div>

    <div class="footer-band"></div>
  </main>
</body>
</html>
```